Cherish Every Note - Days Ring True

I need a website. I had a company doing it, and it looked very nice, but they went way up on hosting costs and said they owned the design of the site. I changed hosts to keep costs down. You can see the current design at farvalecaudio.example. They said I could use the copy and images from the current website. So you could cut and paste to speed things up. My logo and other images are on the current website. If you are unable to use I can send other digital copies.

Target Market(s)

seniors 55 and up

Number of Pages Required

4 page

Font styles to use
Sans Serif

Colors
0255a3
f78f20

Requirements
Must have
• Video testimonies that I can add without assistance. I use youtube links for the videos.
Nice to have
• The color scheme theme can be drawn from the logo, which is on the current webstie farvalecaudio.example
Should not have
• Should not have anything related to TonVo on the website.

```html
<!DOCTYPE html>
<html lang="en">
<head>
<meta charset="utf-8">
<title>Farvale Audio Center – Cherish Every Note</title>
<link rel="stylesheet" href="https://fonts.googleapis.com/css2?family=Marcellus+SC&family=Open+Sans:ital,wght@0,400;0,600;0,700;1,400&family=Lato:wght@400;700&display=swap">
<style>
:root{
  --orange:#f78f20;
  --blue:#0b4aa2;
  --blue-deep:#0a3f8f;
  --ink:#2f2f2f;
  --muted:#666;
  --soft:#eef1f6;
  --footer:#262626;
  --white:#fff;
}
*{box-sizing:border-box;margin:0;padding:0}
html,body{width:1200px;height:4167px;overflow:hidden}
body{position:relative;background:var(--white);font-family:"Lato",sans-serif;color:var(--ink)}
.section{position:absolute;left:0;width:1200px;overflow:hidden}
.abs{position:absolute}
.display{font-family:"Marcellus SC",serif;font-weight:400;color:var(--ink);letter-spacing:1px}
.body-copy{font-family:"Lato",sans-serif;font-size:14px;line-height:29px;color:var(--muted)}
.btn-outline{position:absolute;display:flex;align-items:center;justify-content:center;border:2px solid var(--orange);border-radius:26px;color:var(--orange);font:700 14px "Open Sans",sans-serif;letter-spacing:.3px}

/* top bar */
.topbar{top:0;height:29px;background:var(--orange);color:var(--white);font:600 14px "Open Sans",sans-serif}
.topbar .item{position:absolute;top:0;height:29px;display:flex;align-items:center;gap:7px}
.topbar svg{width:12px;height:12px;fill:var(--white)}

/* header */
.header{top:29px;height:105px;background:var(--white)}
.brand{position:absolute;left:110px;top:24px;display:flex;align-items:center;gap:12px}
.brand-mark{width:56px;height:56px;background:var(--orange)}
.brand-name{font:400 26px/28px "Marcellus SC",serif;color:var(--blue)}
.nav a{position:absolute;top:45px;font:600 15px "Open Sans",sans-serif;color:#333;text-decoration:none}
.nav a.active{color:var(--orange)}
.nav svg{position:absolute;left:1073px;top:48px;width:16px;height:16px}

/* hero */
.hero{top:134px;height:542px;background:linear-gradient(90deg,#7f7772 0%,#a69a90 30%,#c8a48c 55%,#b86d57 75%,#6f3434 100%)}
.hero-title{position:absolute;left:110px;top:135px;font:400 62px/82px "Marcellus SC",serif;color:var(--white);letter-spacing:1px}
.hero-btn{position:absolute;left:113px;top:330px;width:222px;height:50px;border:2px solid var(--white);border-radius:26px;display:flex;align-items:center;justify-content:center;color:var(--white);font:700 15px "Open Sans",sans-serif}
.dots{position:absolute;left:566px;top:461px;display:flex;gap:4px}
.dots span{width:14px;height:14px;border:2px solid var(--white);border-radius:50%}
.dots span.on{background:var(--white)}

/* welcome */
.welcome{top:676px;height:545px}
.portrait{position:absolute;left:112px;top:72px;width:394px;height:394px;border-radius:50%;overflow:hidden;background:radial-gradient(circle at 50% 40%,#d9a49a 0%,#b9b0ab 45%,#9d9d9f 100%)}
.portrait .caption{position:absolute;left:0;bottom:0;width:100%;height:80px;background:rgba(30,30,30,.75);color:var(--white);font:400 20px "Open Sans",sans-serif;text-align:center;padding-top:12px}

/* aids */
.aids{top:1221px;height:542px;background:var(--soft)}
.product{position:absolute;top:369px;width:88px;height:84px;border-radius:40px 40px 20px 20px}

/* tinnitus */
.tinnitus{top:1763px;height:586px}
.chev{position:absolute;width:26px;height:44px}

/* testimonials */
.testimonials{top:2349px;height:611px;background:var(--blue)}
.round-arrow{position:absolute;width:56px;height:56px;border:2px solid var(--white);border-radius:50%;display:flex;align-items:center;justify-content:center}

/* news */
.news{top:2960px;height:657px}
.card-frame{position:absolute;top:230px;width:311px;height:204px;border:1px solid #ddd;padding:5px;background:var(--white)}
.card-frame div{width:100%;height:100%}
.card-title{position:absolute;top:470px;width:320px;font:400 18px/30px "Open Sans",sans-serif;color:#333;white-space:nowrap}
.meta{position:absolute;top:552px;display:flex;align-items:center;gap:7px;font:400 13px "Open Sans",sans-serif;color:#444}
.meta svg{width:12px;height:12px;fill:var(--orange)}

/* footer */
.footer{top:3617px;height:550px;background:linear-gradient(90deg,#1f1f1f 0%,#2c2b2b 55%,#3a3433 100%)}
.footer h3{position:absolute;top:94px;font:600 21px "Open Sans",sans-serif;color:var(--white)}
.field{position:absolute;height:31px;background:var(--white);border:1px solid #ccc;font:400 11px "Open Sans",sans-serif;color:#666;padding:9px 14px}
.submit{position:absolute;left:113px;top:357px;width:113px;height:44px;border-radius:22px;background:var(--orange);color:var(--white);font:700 14px "Open Sans",sans-serif;display:flex;align-items:center;justify-content:center}
.info-ico{position:absolute;left:792px;width:34px;height:34px;border:1px solid #777;border-radius:50%;display:flex;align-items:center;justify-content:center}
.info-ico svg{width:14px;height:14px;fill:var(--orange)}
.info-txt{position:absolute;left:849px;font:400 14px/24px "Open Sans",sans-serif;color:#ddd}
.rule{position:absolute;left:100px;top:438px;width:1000px;height:1px;background:#444}
.copyright{position:absolute;left:110px;top:482px;font:400 13px "Open Sans",sans-serif;color:#ddd}
.social{position:absolute;top:471px;width:42px;height:42px;border:1px solid var(--orange);border-radius:50%}
</style>
</head>
<body>

<div class="section topbar">
  <div class="item" style="left:110px">
    <svg viewBox="0 0 12 12"><path d="M6 0a4 4 0 0 0-4 4c0 3 4 8 4 8s4-5 4-8a4 4 0 0 0-4-4zm0 5.5A1.5 1.5 0 1 1 6 2.5a1.5 1.5 0 0 1 0 3z"/></svg>
    48 Linden Ave, Suite 210, Farvale, NC 28090
  </div>
  <div class="item" style="left:703px">
    <svg viewBox="0 0 12 12"><path d="M2.5 0 4.5 3 3.3 4.3a7 7 0 0 0 4.4 4.4L9 7.5l3 2-1 2.5C5 12 0 7 0 1z"/></svg>
    (555) 014-2290&nbsp;&nbsp;&nbsp;|&nbsp;&nbsp;&nbsp;
    <svg viewBox="0 0 12 12"><path d="M0 2h12v1.2L6 7 0 3.2zM0 4.6l6 3.8 6-3.8V10H0z"/></svg>
    info@farvalecaudio.example
  </div>
</div>

<header class="section header">
  <div class="brand">
    <div class="brand-mark"></div>
    <div class="brand-name">Farvale<br>Audio Center</div>
  </div>
  <nav class="nav">
    <a class="active" style="left:437px">HOME</a>
    <a style="left:511px">HEARING AIDS</a>
    <a style="left:650px">SERVICES</a>
    <a style="left:747px">EDUCATION</a>
    <a style="left:867px">ABOUT US</a>
    <a style="left:972px">CONTACT</a>
    <svg viewBox="0 0 16 16" fill="none" stroke="#333" stroke-width="2.2"><circle cx="6.5" cy="6.5" r="4.8"/><path d="M10 10l5 5"/></svg>
  </nav>
</header>

<section class="section hero" role="img" aria-label="Photo of a smiling young couple embracing at home">
  <h1 class="hero-title">Cherish<br>Every Note</h1>
  <div class="hero-btn">TAKE ACTION TODAY</div>
  <div class="dots"><span class="on"></span><span></span><span></span><span></span></div>
</section>

<section class="section welcome">
  <div class="portrait" role="img" aria-label="Portrait of audiologist Warren Pell">
    <div class="caption">WARREN PELL</div>
  </div>
  <h2 class="display abs" style="left:584px;top:120px;font-size:40px;line-height:54px">WELCOME TO FARVALE<br>AUDIO CENTER LLC</h2>
  <p class="body-copy abs" style="left:584px;top:250px;width:510px">We provide hearing evaluations, counseling, and fitting of hearing aids. We service all the major brands of hearing aids including Audiva, Clearwell, Sonmark, Vireo, Halcyn, Resta, Minttek, Unova, Tessel, Sorbek, and others.</p>
  <div class="btn-outline" style="left:584px;top:400px;width:139px;height:47px">READ MORE</div>
</section>

<section class="section aids">
  <h2 class="display abs" style="left:0;top:84px;width:1200px;text-align:center;font-size:40px;line-height:55px">HEARING AIDS AT<br>FARVALE AUDIO CENTER</h2>
  <p class="body-copy abs" style="left:215px;top:219px;width:770px;text-align:center;line-height:32px">Hearing aids should sound good, look good, and feel good. For most people, hearing loss takes place gradually. Unconsciously, they develop strategies to help them cope better with daily interactions with people, like reading lips, guessing contextually, filling in the blanks, and smiling and faking it.</p>
  <div class="product" style="left:156px;background:linear-gradient(#e4e6e8,#aeb2b6)" role="img" aria-label="Silver hearing aid"></div>
  <div class="product" style="left:289px;background:linear-gradient(#4a4a4c,#141416)" role="img" aria-label="Black hearing aid"></div>
  <div class="product" style="left:422px;background:linear-gradient(#3b4c78,#121c3e)" role="img" aria-label="Navy hearing aid"></div>
  <div class="product" style="left:556px;background:linear-gradient(#d8cfc3,#9c9080)" role="img" aria-label="Beige hearing aid"></div>
  <div class="product" style="left:689px;background:linear-gradient(#dcdedf,#9fa2a6)" role="img" aria-label="Light grey hearing aid"></div>
  <div class="product" style="left:822px;background:linear-gradient(#8a8d90,#3c3e41)" role="img" aria-label="Graphite hearing aid"></div>
  <div class="product" style="left:955px;background:linear-gradient(#8c6a44,#4a2f18)" role="img" aria-label="Bronze hearing aid"></div>
</section>

<section class="section tinnitus">
  <svg class="chev" style="left:36px;top:268px" viewBox="0 0 26 44" fill="none" stroke="#777" stroke-width="3"><path d="M22 4 4 22l18 18"/></svg>
  <h2 class="display abs" style="left:110px;top:112px;font-size:40px">TINNITUS TREATMENT</h2>
  <p class="body-copy abs" style="left:110px;top:184px;width:450px;line-height:31px">More people than ever are seeking help for tinnitus. Tinnitus is a sound that occurs in the brain that no one can hear except the patient. The sounds will vary depending on the patient but are often described as buzzing, ringing, high pitched, ocean sea shell, etc. Usually it is most noticeable at night when going to sleep or early in the day when things are quiet.</p>
  <div class="btn-outline" style="left:112px;top:409px;width:139px;height:49px">READ MORE</div>
  <div class="abs" style="left:629px;top:92px;width:460px;height:395px;background:linear-gradient(120deg,#3a3a3e 0%,#6b6a70 40%,#b9bdc4 75%,#e8e8ea 100%)" role="img" aria-label="Patient wearing headphones during a hearing test in a sound booth"></div>
  <svg class="chev" style="left:1134px;top:268px" viewBox="0 0 26 44" fill="none" stroke="#777" stroke-width="3"><path d="M4 4l18 18L4 40"/></svg>
</section>

<section class="section testimonials">
  <h2 class="display abs" style="left:0;top:70px;width:1200px;text-align:center;font-size:40px;color:var(--white)">TESTIMONIALS</h2>
  <p class="abs" style="left:0;top:147px;width:1200px;text-align:center;font:italic 400 18px 'Open Sans',sans-serif;color:var(--white)">“If you need hearing aids or have a hearing problem, come see Warren Pell.”</p>
  <p class="abs" style="left:0;top:197px;width:1200px;text-align:center;font:400 23px 'Open Sans',sans-serif;color:var(--white)">Glen Ashcroft</p>
  <div class="round-arrow" style="left:244px;top:373px"><svg width="14" height="22" viewBox="0 0 14 22" fill="none" stroke="#fff" stroke-width="2.5"><path d="M11 2 2 11l9 9"/></svg></div>
  <div class="abs" style="left:378px;top:268px;width:444px;height:264px;background:linear-gradient(135deg,#8f8a86 0%,#5b5550 50%,#3d2a22 100%)" role="img" aria-label="Video testimonial of a satisfied patient in the clinic office">
    <svg class="abs" style="left:191px;top:100px" width="62" height="62" viewBox="0 0 62 62"><circle cx="31" cy="31" r="29" fill="none" stroke="#fff" stroke-width="3"/><path d="M24 18v26l21-13z" fill="#fff"/></svg>
  </div>
  <div class="round-arrow" style="left:896px;top:373px"><svg width="14" height="22" viewBox="0 0 14 22" fill="none" stroke="#fff" stroke-width="2.5"><path d="M3 2l9 9-9 9"/></svg></div>
</section>

<section class="section news">
  <h2 class="display abs" style="left:0;top:95px;width:1200px;text-align:center;font-size:40px">WHAT’S NEW IN HEARING HEALTH?</h2>
  <p class="abs" style="left:0;top:168px;width:1200px;text-align:center;font:400 15px 'Lato',sans-serif;color:var(--muted)">Learn more about hearing healthcare through the articles below</p>

  <div class="card-frame" style="left:110px"><div role="img" aria-label="Couple launching a red canoe at a lake" style="background:linear-gradient(180deg,#e9dcc4 0%,#8d7a61 55%,#8b2a2a 85%,#3c3a3a 100%)"></div></div>
  <div class="card-frame" style="left:444px"><div role="img" aria-label="Joyful woman with arms raised outdoors" style="background:linear-gradient(180deg,#6f7b86 0%,#8e9a8c 50%,#3f4a3c 100%)"></div></div>
  <div class="card-frame" style="left:779px"><div role="img" aria-label="Card payment at a store counter" style="background:linear-gradient(135deg,#b86a2a 0%,#6d3a17 50%,#1e1612 100%)"></div></div>

  <p class="card-title" style="left:110px">Do's and Don'ts for Communicating<br>During the Holidays</p>
  <p class="card-title" style="left:445px">Communication for All: How<br>People of All Ages Benefit</p>
  <p class="card-title" style="left:780px">Over-the-Counter Hearing<br>Aids: What You Need to Know</p>

  <div class="meta" style="left:110px"><svg viewBox="0 0 12 12"><path d="M1 2h10v10H1zM3 0h1.5v3H3zM7.5 0H9v3H7.5zM2 5v6h8V5z"/></svg>12/19/2019 &nbsp;|&nbsp; <svg viewBox="0 0 12 12"><circle cx="6" cy="3.3" r="3"/><path d="M0 12a6 5 0 0 1 12 0z"/></svg>John Doe</div>
  <div class="meta" style="left:445px"><svg viewBox="0 0 12 12"><path d="M1 2h10v10H1zM3 0h1.5v3H3zM7.5 0H9v3H7.5zM2 5v6h8V5z"/></svg>12/19/2019 &nbsp;|&nbsp; <svg viewBox="0 0 12 12"><circle cx="6" cy="3.3" r="3"/><path d="M0 12a6 5 0 0 1 12 0z"/></svg>John Doe</div>
  <div class="meta" style="left:780px"><svg viewBox="0 0 12 12"><path d="M1 2h10v10H1zM3 0h1.5v3H3zM7.5 0H9v3H7.5zM2 5v6h8V5z"/></svg>12/19/2019 &nbsp;|&nbsp; <svg viewBox="0 0 12 12"><circle cx="6" cy="3.3" r="3"/><path d="M0 12a6 5 0 0 1 12 0z"/></svg>John Doe</div>
</section>

<footer class="section footer">
  <h3 style="left:110px">CONTACT US</h3>
  <div class="field" style="left:113px;top:165px;width:309px">First Name</div>
  <div class="field" style="left:432px;top:165px;width:309px">Last Name</div>
  <div class="field" style="left:113px;top:210px;width:309px">Email</div>
  <div class="field" style="left:432px;top:210px;width:309px">Phone Number</div>
  <div class="field" style="left:113px;top:257px;width:628px;height:81px">Comments</div>
  <div class="submit">SUBMIT</div>

  <h3 style="left:791px">CONTACT INFORMATION</h3>
  <div class="info-ico" style="top:159px"><svg viewBox="0 0 12 12"><path d="M6 0a4 4 0 0 0-4 4c0 3 4 8 4 8s4-5 4-8a4 4 0 0 0-4-4zm0 5.5A1.5 1.5 0 1 1 6 2.5a1.5 1.5 0 0 1 0 3z"/></svg></div>
  <div class="info-txt" style="top:155px">48 Linden Ave<br>Suite 210 Farvale, NC 28090</div>
  <div class="info-ico" style="top:231px"><svg viewBox="0 0 12 12"><path d="M2.5 0 4.5 3 3.3 4.3a7 7 0 0 0 4.4 4.4L9 7.5l3 2-1 2.5C5 12 0 7 0 1z"/></svg></div>
  <div class="info-txt" style="top:236px">(555) 014-2290</div>
  <div class="info-ico" style="top:289px"><svg viewBox="0 0 12 12"><path d="M3 0h6v3H3zM0 4h12v6h-2v2H2v-2H0zM3 8v3h6V8z"/></svg></div>
  <div class="info-txt" style="top:294px">+1 222 222 2222</div>
  <div class="info-ico" style="top:347px"><svg viewBox="0 0 12 12"><path d="M0 2h12v1.2L6 7 0 3.2zM0 4.6l6 3.8 6-3.8V10H0z"/></svg></div>
  <div class="info-txt" style="top:352px">info@farvalecaudio.example</div>

  <div class="rule"></div>
  <p class="copyright">Copyright © 2019, Farvale Audio Center. All right reserved.</p>
  <div class="social" style="left:846px" aria-label="Social profile link"></div>
  <div class="social" style="left:895px" aria-label="Social profile link"></div>
  <div class="social" style="left:945px" aria-label="Social profile link"></div>
  <div class="social" style="left:995px" aria-label="Social profile link"></div>
  <div class="social" style="left:1045px" aria-label="Social profile link"></div>
</footer>

</body>
</html>
```